One of Australia's fastest growing Financial Company looking for an updated business card design!

Meridale Holdings Australia is looking for an updated design for our business cards. We would like to keep up our professional appearances and have get new exciting design that fits our company.

The Meridale aim is to facilitate and assist clients in every financial requirement that may arise in financial areas.

We would to see the design to use colour blue and we like the clouds in the background. We have attached two designs we have use before but we need something with more professional and easy to read design.

We would like the website in the back of the card; the employees name more central and stands out; only a postal address; a list of all our locations along the bottom (Sydney, Melbourne, Brisbane, Singapore)

Looking forward to seeing the designs come in!

Target Market(s)

Other Industry Professionals
Middle Class Families

Industry/Entity Type

Finance

Contact Information for Business Card

Name; Company Role; Office Number; Mobile Number; Email Address; Website; Postal Address; Locations

Font styles to use
Serif
Sans Serif

Colors
0492cd
33a6d7
85cae6
85acd3
3176b5
0455a3
cee9f5
d5e2ee

Requirements
Must have
• Name; Company Role; Office Number; Mobile Number; Email Address; Website; Postal Address; Locations
Nice to have
• The colour blue, clouds on the background

```html
<!DOCTYPE html>
<html lang="en">
<head>
<meta charset="utf-8">
<title>Meridale Holdings Australia – Business Card</title>
<link rel="stylesheet" href="https://fonts.googleapis.com/css2?family=Open+Sans:ital,wght@0,400;0,600;0,700;1,400&family=Arimo:wght@400;700&display=swap">
<style>
  :root {
    --stage: #bcbdbf;
    --sky-top: #229bd8;
    --sky-bottom: #1d84c8;
    --navy-band: #0455a3;
    --band-lip: #1f74bb;
    --brand-blue: #1f8fd3;
    --title-blue: #1f5fae;
    --ink: #111111;
    --accent-red: #e8383d;
    --white: #ffffff;
  }
  * { margin: 0; padding: 0; box-sizing: border-box; }
  html, body { width: 961px; height: 1200px; overflow: hidden; }
  body { background: var(--stage); position: relative; font-family: "Arimo", Arial, sans-serif; }

  .card {
    position: absolute;
    left: 111px;
    width: 739px;
    border-radius: 34px;
    overflow: hidden;
    box-shadow: 0 6px 14px rgba(0,0,0,0.28);
  }

  /* Front */
  .card--front {
    top: 111px;
    height: 451px;
    background: linear-gradient(180deg, var(--sky-top) 0%, var(--sky-bottom) 100%);
  }
  .card--front .brand {
    position: absolute;
    left: 0; right: 0;
    top: 155px;
    text-align: center;
    font-family: "Open Sans", Arial, sans-serif;
    font-weight: 600;
    font-size: 112px;
    line-height: 1;
    letter-spacing: -2px;
    color: var(--white);
  }
  .web-band {
    position: absolute;
    left: 0; right: 0;
    top: 371px;
    height: 60px;
    background: var(--navy-band);
    color: var(--white);
    font-family: "Arimo", Arial, sans-serif;
    font-weight: 700;
    font-size: 22px;
    letter-spacing: 0.3px;
    display: flex;
    align-items: center;
    justify-content: center;
  }
  .web-lip {
    position: absolute;
    left: 0; right: 0;
    top: 431px;
    height: 20px;
    background: var(--band-lip);
  }

  /* Back */
  .card--back {
    top: 637px;
    height: 452px;
    background: var(--white);
  }
  .card--back .brand {
    position: absolute;
    right: 40px;
    top: 40px;
    font-family: "Open Sans", Arial, sans-serif;
    font-weight: 600;
    font-size: 84px;
    line-height: 1;
    letter-spacing: -1.5px;
    color: var(--brand-blue);
  }
  .role {
    position: absolute;
    left: 28px;
    top: 180px;
    font-family: "Arimo", Arial, sans-serif;
    font-style: italic;
    font-size: 21px;
    color: var(--title-blue);
  }
  .person {
    position: absolute;
    left: 28px;
    top: 207px;
    font-family: "Open Sans", Arial, sans-serif;
    font-weight: 700;
    font-size: 29px;
    letter-spacing: 0.2px;
    color: var(--ink);
  }
  .rule {
    position: absolute;
    left: 28px;
    right: 28px;
    top: 244px;
    height: 2px;
    background: var(--ink);
  }
  .contact-list {
    position: absolute;
    left: 28px;
    top: 262px;
    list-style: none;
    font-size: 21px;
    color: var(--ink);
  }
  .contact-list li {
    display: flex;
    align-items: center;
    height: 29.5px;
  }
  .contact-list svg { width: 20px; height: 20px; margin-right: 9px; flex: none; }
  .postal {
    position: absolute;
    right: 28px;
    top: 262px;
    font-style: normal;
    text-align: right;
    font-size: 21px;
    line-height: 29.5px;
    color: var(--ink);
  }
  .locations {
    position: absolute;
    left: 0; right: 0;
    top: 373px;
    height: 79px;
    border-top: 7px solid var(--navy-band);
    background: linear-gradient(180deg, var(--sky-top) 0%, var(--sky-bottom) 100%);
    display: flex;
    align-items: center;
    justify-content: center;
    gap: 16px;
    font-family: "Open Sans", Arial, sans-serif;
    font-weight: 700;
    font-size: 21px;
    letter-spacing: 0.8px;
    color: var(--white);
  }
  .locations .sep { font-weight: 400; }
</style>
</head>
<body>

  <section class="card card--front" aria-label="Business card front">
    <div class="brand">Meridale</div>
    <div class="web-band">MeridaleInvestmentsGroup.com.au</div>
    <div class="web-lip"></div>
  </section>

  <section class="card card--back" aria-label="Business card back">
    <div class="brand">Meridale</div>

    <p class="role">Investment Consultant</p>
    <h1 class="person">CLAIRE HOLLINS</h1>
    <div class="rule"></div>

    <ul class="contact-list">
      <li>
        <svg viewBox="0 0 24 24" aria-hidden="true"><path fill="var(--accent-red)" d="M6.6 10.8a15.5 15.5 0 0 0 6.6 6.6l2.2-2.2c.3-.3.7-.4 1-.2 1.1.4 2.3.6 3.6.6.6 0 1 .4 1 1V20c0 .6-.4 1-1 1A17 17 0 0 1 3 4c0-.6.4-1 1-1h3.5c.6 0 1 .4 1 1 0 1.3.2 2.5.6 3.6.1.3 0 .7-.2 1z"/></svg>
        (02) 6500 4100
      </li>
      <li>
        <svg viewBox="0 0 24 24" aria-hidden="true"><rect x="5" y="1.5" width="14" height="21" rx="2.5" fill="var(--accent-red)"/><rect x="7.5" y="4.5" width="9" height="12" fill="#fff"/><circle cx="12" cy="19.3" r="1.3" fill="#fff"/></svg>
        (02) 6500 7720
      </li>
      <li>
        <svg viewBox="0 0 24 24" aria-hidden="true"><rect x="1" y="4.5" width="22" height="15" fill="var(--accent-red)"/><path d="M1.5 5.5 12 13.5 22.5 5.5M1.5 18.5l8-7M22.5 18.5l-8-7" stroke="#fff" stroke-width="1.4" fill="none"/></svg>
        info@MeridaleHoldingsAustralia.com.au
      </li>
    </ul>

    <address class="postal">
      Harbourview Post Shop<br>
      PO BOX 456<br>
      Harbourview 2999
    </address>

    <div class="locations">
      <span>SYDNEY</span><span class="sep">|</span>
      <span>MELBOURNE</span><span class="sep">|</span>
      <span>BRISBANE</span><span class="sep">|</span>
      <span>SINGAPORE</span>
    </div>
  </section>

</body>
</html>
```